Business card for Chicago based Private Equity Company

We need a business card for our PE company called Crestline Holdings. We want a simple and clean, yet creative card design. The back side should reflect our logo. Also would like to see embossed ideas. Should reflect strength and growth. Our logo is attached. Also need editable file. Details are as follows for Business Card:

Dana Welmore Co-Founder 2750 Marlow Avenue Suite 410 Fernvale, IL 60914 http://www.crestlineholdingsllc.example (D) 630.555.0147 (C) 312.555.0182 (E) dw@crestlineholdingsllc.example

```html
<!DOCTYPE html>
<html lang="en">
<head>
<meta charset="utf-8">
<title>Crestline Holdings — Business Card</title>
<link rel="stylesheet" href="https://fonts.googleapis.com/css2?family=PT+Sans:wght@400;700&display=swap">
<style>
  :root {
    --backdrop: #8e8e8e;
    --card: #0b0b0b;
    --ink: #f4f4f2;
    --muted: #a8a8a8;
  }
  * { margin: 0; padding: 0; box-sizing: border-box; }
  html, body {
    width: 1200px; height: 900px; overflow: hidden;
    background: var(--backdrop);
    font-family: "PT Sans", Arial, sans-serif;
  }
  .canvas {
    position: relative; width: 1200px; height: 900px;
    display: flex; align-items: center; justify-content: center; gap: 40px;
  }
  .card {
    position: relative; width: 540px; height: 310px;
    background: var(--card); color: var(--ink);
    box-shadow: 0 6px 18px rgba(0,0,0,0.35);
  }
  /* Front */
  .brand {
    position: absolute; left: 34px; top: 34px;
    display: flex; align-items: center; gap: 14px;
  }
  .brand-mark {
    width: 52px; height: 52px; border-radius: 50%;
    border: 5px solid var(--ink);
  }
  .brand-name {
    font-weight: 700; font-size: 26px; letter-spacing: 3px;
    text-transform: uppercase; color: var(--ink);
  }
  .holder { position: absolute; left: 34px; top: 124px; }
  .holder-name { font-weight: 700; font-size: 30px; line-height: 1.1; }
  .holder-title { font-weight: 700; font-size: 16px; color: var(--muted); margin-top: 4px; }
  .contact {
    position: absolute; right: 30px; bottom: 28px;
    font-weight: 700; font-size: 13.5px; line-height: 1.55; text-align: right;
  }
  .contact-line { display: block; }
  .contact-lines { text-align: left; margin-top: 2px; }
  .contact-label { display: inline-block; width: 22px; }
  /* Back */
  .card-back { display: flex; align-items: center; justify-content: center; }
  .back-brand { display: flex; align-items: center; gap: 18px; }
  .back-mark {
    width: 92px; height: 92px; border-radius: 50%;
    background: var(--ink);
  }
  .back-name {
    font-weight: 700; font-size: 30px; letter-spacing: 4px;
    text-transform: uppercase; color: var(--ink); line-height: 1.15;
  }
</style>
</head>
<body>
<main class="canvas">
  <section class="card card-front" aria-label="Card front">
    <div class="brand">
      <span class="brand-mark" aria-hidden="true"></span>
      <span class="brand-name">Crestline Holdings</span>
    </div>
    <div class="holder">
      <p class="holder-name">Dana Welmore</p>
      <p class="holder-title">Co-Founder</p>
    </div>
    <address class="contact" style="font-style:normal">
      <span class="contact-line">2750 Marlow Avenue Suite 410</span>
      <span class="contact-line">Fernvale, IL 60914</span>
      <span class="contact-line">www.crestlineholdingsllc.example</span>
      <span class="contact-lines">
        <span class="contact-line"><span class="contact-label">D</span>630.555.0147</span>
        <span class="contact-line"><span class="contact-label">C</span>312.555.0182</span>
        <span class="contact-line"><span class="contact-label">E</span>dw@crestlineholdingsllc.example</span>
      </span>
    </address>
  </section>

  <section class="card card-back" aria-label="Card back">
    <div class="back-brand">
      <span class="back-mark" aria-hidden="true"></span>
      <span class="back-name">Crestline<br>Holdings</span>
    </div>
  </section>
</main>
</body>
</html>
```